CREATIVE DESIGNERS NEEDED & Enhance Your Business Card Portfolio

Artistic, unique, professional real estate card needed - see attached documents "B-cards.pdf" for all details and examples.True Designers will see other projects of ours come online here. We like long-term relationships for creative designers. This business card will be used in two U.S. states and is central to our business and other future marketing.

Target Market(s)

Buyers and Sellers of real estate

Industry/Entity Type

Real Estate Agent

Contact Information for Business Card

See attached detailed brief

Font styles to use
Other font styles liked:
• ADAM.CG PRO & NewsGoth BT

Requirements
Must have
• 2-sided, creative (non-traditional layout/design). Incorporate a cut-out (for texture, and make it fun! No boring templates for this card -
Nice to have
• See attached detailed brief
Should not have

```html
<!DOCTYPE html>
<html lang="en">
<head>
<meta charset="utf-8">
<title>Kade Lorne Group Real Estate – Business Card</title>
<link href="https://fonts.googleapis.com/css2?family=Montserrat:wght@500;700&family=Libre+Franklin:wght@400;600&display=swap" rel="stylesheet">
<style>
  :root {
    --backdrop: #3b3b3d;
    --navy: #2b3a4c;
    --navy-gloss: #4a5a6e;
    --ink: #2a3547;
    --red: #c8282d;
    --paper: #ffffff;
    --muted: #5b6470;
    --front-text: #e8ecf0;
  }
  * { box-sizing: border-box; margin: 0; padding: 0; }
  html, body { width: 800px; height: 1200px; overflow: hidden; }
  body {
    background: var(--backdrop);
    font-family: "Libre Franklin", Arial, sans-serif;
    position: relative;
  }
  .card {
    position: absolute;
    left: 50px;
    width: 700px;
    height: 400px;
    overflow: hidden;
  }
  .card-front { top: 90px; background: var(--navy); }
  .card-back { top: 690px; background: var(--paper); }

  /* Brand name block */
  .brand { position: absolute; display: flex; align-items: center; gap: 14px; }
  .brand-square { width: 62px; height: 62px; flex: none; }
  .brand-name {
    font-family: "Montserrat", Arial, sans-serif;
    font-weight: 700;
    line-height: 1;
    letter-spacing: 1px;
  }
  .brand-name span { display: block; }
  .brand-name .big { font-size: 46px; }
  .brand-name .small { font-size: 20px; margin-top: 4px; letter-spacing: 2px; }
  .brand-name .tiny { font-size: 15px; margin-top: 3px; letter-spacing: 4px; }

  .card-front .brand { left: 80px; top: 70px; }
  .card-front .brand-square { background: var(--navy-gloss); }
  .card-front .brand-name { color: var(--navy-gloss); }

  .tagline {
    position: absolute; left: 80px; top: 205px;
    color: var(--red); font-size: 21px; letter-spacing: 0.5px;
  }
  .addresses { position: absolute; left: 80px; top: 245px; display: flex; gap: 50px; }
  .address { display: flex; gap: 8px; color: var(--front-text); font-size: 18px; line-height: 1.35; }
  .address svg { flex: none; margin-top: 2px; }

  /* Back */
  .card-back .brand { left: 36px; top: 32px; }
  .card-back .brand-square { background: var(--red); }
  .card-back .brand-name { color: var(--ink); }
  .markets {
    position: absolute; left: 40px; top: 128px;
    font-family: "Montserrat", Arial, sans-serif; font-weight: 500;
    font-size: 12px; letter-spacing: 5px; color: var(--ink);
  }
  .agent-name {
    position: absolute; left: 40px; top: 158px;
    font-family: "Montserrat", Arial, sans-serif; font-weight: 700;
    font-size: 24px; letter-spacing: 1px; color: var(--ink);
  }
  .agent-title {
    position: absolute; left: 40px; top: 190px;
    font-weight: 600; font-size: 15px; color: var(--red);
  }
  .contacts { position: absolute; top: 222px; display: flex; flex-direction: column; gap: 6px; }
  .contacts.phones { left: 40px; }
  .contacts.online { left: 200px; top: 248px; }
  .contact { display: flex; align-items: center; gap: 7px; font-size: 15px; color: var(--ink); }
  .licenses {
    position: absolute; left: 212px; top: 318px;
    font-size: 12px; color: var(--muted); line-height: 1.4;
  }
  .badges { position: absolute; left: 40px; top: 290px; display: flex; gap: 10px; align-items: center; }
  .badge { background: #d5d8dc; }
  .badge.house { width: 30px; height: 30px; }
  .badge.square { width: 30px; height: 34px; }
  .badge.wide { width: 40px; height: 20px; }
  .portrait-area {
    position: absolute; right: 0; top: 60px; width: 220px; height: 340px;
    background: linear-gradient(100deg, rgba(255,255,255,0) 0%, #9aa3ae 35%, #3a4658 75%, #2a3547 100%);
  }
</style>
</head>
<body>

<section class="card card-front">
  <div class="brand">
    <div class="brand-square"></div>
    <div class="brand-name">
      <span class="big">KADE</span>
      <span class="small">LORNE GROUP</span>
      <span class="tiny">REAL ESTATE</span>
    </div>
  </div>
  <p class="tagline">RESIDENTIAL. INVESTMENT. DEVELOPMENT.</p>
  <div class="addresses">
    <div class="address">
      <svg width="16" height="16" viewBox="0 0 16 16" aria-hidden="true"><circle cx="8" cy="8" r="7.5" fill="var(--red)"/><path d="M8 3.5a3 3 0 0 0-3 3c0 2.2 3 5.5 3 5.5s3-3.3 3-5.5a3 3 0 0 0-3-3z" fill="var(--navy)"/><circle cx="8" cy="6.5" r="1" fill="var(--red)"/></svg>
      <p>418 Harbor View Lane<br>San Diego, CA 92104</p>
    </div>
    <div class="address">
      <svg width="16" height="16" viewBox="0 0 16 16" aria-hidden="true"><circle cx="8" cy="8" r="7.5" fill="var(--red)"/><path d="M8 3.5a3 3 0 0 0-3 3c0 2.2 3 5.5 3 5.5s3-3.3 3-5.5a3 3 0 0 0-3-3z" fill="var(--navy)"/><circle cx="8" cy="6.5" r="1" fill="var(--red)"/></svg>
      <p>2750 W. Palo Verde Ave<br>#C Goodyear, AZ 85338</p>
    </div>
  </div>
</section>

<section class="card card-back">
  <div class="brand">
    <div class="brand-square"></div>
    <div class="brand-name">
      <span class="big">KADE</span>
      <span class="small">LORNE GROUP</span>
    </div>
  </div>
  <p class="markets">SAN DIEGO &amp; PHOENIX</p>
  <h1 class="agent-name">KADE LORNE</h1>
  <p class="agent-title">Broker Associate &amp; Realtor</p>

  <div class="contacts phones">
    <p class="contact">
      <svg width="15" height="15" viewBox="0 0 16 16" aria-hidden="true"><circle cx="8" cy="8" r="7" fill="none" stroke="var(--red)" stroke-width="1.3"/><path d="M5.5 4.5l1.3 1.6-.7 1a4 4 0 0 0 2 2l1-.7 1.6 1.3-.6 1.2c-3 0-5.7-2.7-5.7-5.7z" fill="var(--red)"/></svg>
      (855) HOME-NOW
    </p>
    <p class="contact">
      <svg width="15" height="15" viewBox="0 0 16 16" aria-hidden="true"><circle cx="8" cy="8" r="7" fill="none" stroke="var(--red)" stroke-width="1.3"/><rect x="5.5" y="4" width="5" height="8" rx="1" fill="var(--red)"/></svg>
      (619) 555-0187
    </p>
  </div>

  <div class="contacts online">
    <p class="contact">
      <svg width="15" height="15" viewBox="0 0 16 16" aria-hidden="true"><circle cx="8" cy="8" r="7.5" fill="var(--red)"/><rect x="4" y="5.5" width="8" height="5" fill="#fff"/><path d="M4 5.5l4 3 4-3" fill="none" stroke="var(--red)" stroke-width="0.9"/></svg>
      Kade@KadeLorneGroup.com
    </p>
    <p class="contact">
      <svg width="15" height="15" viewBox="0 0 16 16" aria-hidden="true"><circle cx="8" cy="8" r="7.5" fill="var(--red)"/><rect x="4" y="5.5" width="8" height="5" fill="#fff"/></svg>
      IG: @KadeLorneRealEstate
    </p>
  </div>

  <p class="licenses">CAL BRE 02471958<br>AZ BR 538204117</p>

  <div class="badges">
    <div class="badge house"></div>
    <div class="badge square"></div>
    <div class="badge wide"></div>
  </div>

  <div class="portrait-area" role="img" aria-label="Halftone portrait of the agent"></div>
</section>

</body>
</html>
```